Website design needed for gift based dropship website

I am building a dropshipping website that will create gift based merchandise and send it out to our clients customers for them. Our clients will sell products and when a customer buys from them, we create the item and send it out to the customer.

I am looking for a very similar website to quillmarten.com - that website is doing a very similar thing to what i am doing but where the quillmarten website is based around clothing, my website will be based around gifts. Another website that i like that is doing a similar thing to what i will do is dravo.com

I require 2 pages to be made:
1) The home page
2) A landing page for a free product giveaway offer

1) THE HOME PAGE
The home page should be a merger of the two previously stated websites (www.dravo.com and www.quillmarten.com). The style fo the homepage should be based on the logo that is attached and the colour scheme should be similar but basic.

2) THE LANDING PAGE
The landing page will be giving away a free mobile phone cover. The page needs to have some mobile phone covers for different phones all with random designs on. The page should state that they can have any design that they want and they do not pay for the phone (they only pay for shipping).

Menu pages and text should be taken from the quillmarten.com website.

Target Market(s)

18 - 40 year old males. People who like the idea of earning extra money in their spare time but aren't too sure how to do it. Semi-professional jobs.

Number of Pages Required

2 page

Font styles to use
Serif
Sans Serif
Decorative
Script

Colors

Designer to choose colors to be used in the design.

Requirements
Must have
• A "how it works" image where the dropshipping process is explained to a visitor to the website (similar to the one on the quillmarten "how it works page")
Nice to have
• Testimonial area on homepage
Should not have
• Homepage should not have:
• - "latest orders from" area
• - Video
• - Warehousing/fulfilment area
• - Integration area
• -

```html
<!DOCTYPE html>
<html lang="en">
<head>
<meta charset="utf-8">
<title>Kindred Prints – Free Mobile Phone Cover</title>
<link rel="stylesheet" href="https://fonts.googleapis.com/css2?family=Roboto+Condensed:wght@400;700&family=Roboto:wght@400;500;700&family=Caveat:wght@400;600&display=swap">
<style>
:root{
  --red:#e3140c;
  --maroon:#3f1822;
  --maroon-soft:#5a2430;
  --ink:#222;
  --muted:#8a8a8a;
  --hero-bg:#e5e3e3;
  --card-bg:#f3f3f3;
  --card-line:#d6d6d6;
  --footer-bg:#e4e2e2;
  --white:#fff;
}
*{box-sizing:border-box;margin:0;padding:0}
html,body{width:1200px;height:4688px;overflow:hidden}
body{position:relative;background:var(--white);font-family:"Roboto",Arial,sans-serif;color:var(--ink)}
.abs{position:absolute}
.heading{font-family:"Roboto Condensed","Arial Narrow",sans-serif;font-weight:700;color:var(--maroon-soft);text-align:center;width:1200px;left:0}
.subheading{color:var(--muted);text-align:center;font-size:28px;line-height:34px;width:1200px;left:0}
.script{font-family:"Caveat",cursive;color:var(--red)}
.btn{position:absolute;background:var(--red);color:var(--white);font-family:"Roboto Condensed",sans-serif;font-weight:700;display:flex;align-items:center;justify-content:center;font-size:22px}

/* header */
.topbar{top:0;left:0;width:1200px;height:40px;background:linear-gradient(#f1f1f1,#fff)}
.account{top:6px;right:56px;font-size:17px;color:#444;display:flex;gap:40px}
.brand{display:flex;align-items:center;gap:16px}
.brand-mark{width:56px;height:56px;border-radius:50%;background:var(--red)}
.brand-name{font-family:"Roboto Condensed",sans-serif;font-weight:700;font-size:40px;color:var(--maroon);line-height:1}
.site-logo{top:86px;left:150px}
.main-nav{top:50px;left:430px;display:flex;gap:36px;font-size:18px;color:var(--ink)}
.social{top:132px;left:776px;display:flex;align-items:center;gap:20px}
.social .script{font-size:28px}
.social-dot{width:20px;height:20px;border-radius:50%;background:var(--red)}

/* hero */
.hero{top:206px;left:0;width:1200px;height:660px;background:var(--hero-bg)}
.hero-kicker{top:280px;left:125px;font-size:54px;display:flex;align-items:center;gap:12px}
.hero-title{top:370px;left:125px;font-family:"Roboto Condensed",sans-serif;font-weight:700;font-size:82px;line-height:88px;color:var(--maroon)}
.hero-title .free{color:var(--red)}
.hero-text{top:560px;left:125px;width:540px;font-size:27px;line-height:40px;color:#333}
.hero-btn{top:694px;left:125px;width:394px;height:66px;font-size:24px}
.cover{position:absolute;border-radius:34px;border:8px solid #d8d8d8;box-shadow:0 8px 18px rgba(0,0,0,.25)}

/* sections */
.section-bg{top:866px;left:0;width:1200px;height:1394px;background:linear-gradient(#fff 0,#fff 55%,#eeeeee 100%)}
.divider{position:absolute;height:3px;background:var(--maroon-soft)}
.badge{position:absolute;width:108px;height:108px;border-radius:50%;background:var(--maroon);display:flex;align-items:center;justify-content:center}
.card{position:absolute;width:279px;height:344px;background:var(--card-bg);border:2px solid var(--card-line);display:flex;align-items:center;justify-content:center}
.phone{width:118px;height:270px;border-radius:22px;border:6px solid #cfcfcf}
.phone.dark{border-color:#444}
.card-title{position:absolute;width:279px;text-align:center;font-family:"Roboto Condensed",sans-serif;font-weight:700;font-size:25px;color:var(--ink)}
.card-sub{position:absolute;width:279px;text-align:center;font-size:13px;color:#555}
.pattern{position:absolute;width:170px;height:172px}
.or{position:absolute;top:2978px;left:569px;width:62px;height:62px;border-radius:50%;border:3px solid #e1e1e1;background:#fff;display:flex;align-items:center;justify-content:center;font-size:28px;font-weight:700;color:var(--ink)}
.upload-field{position:absolute;top:3088px;left:269px;width:381px;height:53px;background:#eeeeee;border:1px solid #dcdcdc;display:flex;align-items:center;gap:12px;padding-left:16px;font-size:18px;color:#999}
.cloud{width:24px;height:16px;border-radius:8px;background:#bbb}
.hint{position:absolute;top:3146px;left:309px;font-size:11px;color:#999}
.select{position:absolute;width:156px;height:28px;border:1px solid #cfcfcf;background:#fff;font-size:14px;color:#555;display:flex;align-items:center;padding-left:14px}
.select::after{content:"";position:absolute;right:0;top:0;width:26px;height:26px;background:#ececec}
.submit-box{position:absolute;top:4119px;left:147px;width:894px;height:140px;border:2px solid #dcdcdc;background:#fafafa}
.postage{top:4316px;font-size:21px;color:var(--muted)}

/* footer */
.footer{top:4406px;left:0;width:1200px;height:244px;background:var(--footer-bg)}
.footer-logo{top:4460px;left:150px}
.footer-logo .brand-mark{width:48px;height:48px}
.footer-logo .brand-name{font-size:34px}
.footer-phone{top:4590px;left:150px;display:flex;align-items:center;gap:12px;font-size:26px;font-weight:700;color:var(--maroon)}
.footer-col{position:absolute;top:4456px;font-size:12px;line-height:27px;color:#555}
.footer-col h4{font-size:15px;font-weight:700;color:var(--maroon);letter-spacing:.5px;margin-bottom:6px}
.legal{top:4650px;left:0;width:1200px;height:38px;background:var(--red);color:#fff;font-size:12px;display:flex;align-items:center;justify-content:flex-end;padding-right:150px}
</style>
</head>
<body>

<header>
  <div class="abs topbar"></div>
  <div class="abs account"><span>⊕ Login</span><span>+ Sign up</span></div>
  <div class="abs brand site-logo"><span class="brand-mark"></span><span class="brand-name">Kindred Prints</span></div>
  <nav class="abs main-nav"><span>Products</span><span>How it works</span><span>Mockup Generator</span><span>Shipping</span><span>FAQ</span><span>Blog</span></nav>
  <div class="abs social"><span class="script">Social Media →</span><span class="social-dot"></span><span class="social-dot"></span><span class="social-dot"></span></div>
</header>

<section>
  <div class="abs hero"></div>
  <div class="abs hero-kicker script"><span>get your</span>
    <svg width="54" height="24" viewBox="0 0 54 24"><path d="M2 14 Q26 6 48 12 M38 4 L50 12 L40 20" fill="none" stroke="#e3140c" stroke-width="3" stroke-linecap="round"/></svg></div>
  <h1 class="abs hero-title"><span class="free">Free</span> Mobile<br>Phone Cover!</h1>
  <p class="abs hero-text">Choose from one of our designs or create your own and only pay for the shipping</p>
  <div class="btn hero-btn">Create your own design now!</div>
  <div class="cover" role="img" aria-label="Phone cover with a bright summer fruit illustration" style="top:250px;left:756px;width:256px;height:452px;background:linear-gradient(160deg,#f7d23a,#f4c21c 60%,#ee6b4a)"></div>
  <div class="cover" role="img" aria-label="Phone cover with a black and white doodle pattern" style="top:390px;left:904px;width:180px;height:380px;border-color:#333;background:linear-gradient(160deg,#f4f4f4,#bdbdbd)"></div>
  <div class="cover" role="img" aria-label="Phone cover with a painted portrait in purple tones" style="top:476px;left:690px;width:190px;height:352px;background:linear-gradient(160deg,#b04a9a,#6b2a8c 55%,#e84a6a)"></div>
</section>

<section>
  <div class="abs section-bg"></div>
  <div class="divider" style="top:976px;left:150px;width:363px"></div>
  <div class="divider" style="top:976px;left:681px;width:369px"></div>
  <div class="badge" style="top:924px;left:543px">
    <svg width="40" height="56" viewBox="0 0 40 56"><rect x="3" y="2" width="34" height="52" rx="5" fill="none" stroke="#fff" stroke-width="4"/><circle cx="20" cy="46" r="3" fill="#fff"/></svg></div>
  <h2 class="abs heading" style="top:1060px;font-size:62px">Choose from a range of phone covers</h2>
  <p class="abs subheading" style="top:1138px">Pick one of our designs or upload your own</p>

  <div class="card" style="top:1225px;left:137px"><div class="phone" role="img" aria-label="Purple starfield cover design" style="background:linear-gradient(160deg,#8a2aa0,#3d2a8a)"></div></div>
  <div class="card" style="top:1225px;left:453px"><div class="phone" role="img" aria-label="Pale blue leaf pattern cover design" style="background:linear-gradient(160deg,#cbd9e0,#a8bfca)"></div></div>
  <div class="card" style="top:1225px;left:769px"><div class="phone dark" role="img" aria-label="Colourful cartoon character cover design" style="background:linear-gradient(160deg,#e04a4a,#3e6fb8 60%,#f0c040)"></div></div>
  <div class="card-title" style="top:1578px;left:137px">Lumo Covers</div><div class="card-sub" style="top:1608px;left:137px">Lumo 6/6s</div>
  <div class="card-title" style="top:1578px;left:453px">Lumo Covers</div><div class="card-sub" style="top:1608px;left:453px">Lumo 7/8</div>
  <div class="card-title" style="top:1578px;left:769px">Lumo Covers</div><div class="card-sub" style="top:1608px;left:769px">Lumo X</div>

  <div class="card" style="top:1678px;left:137px"><div class="phone dark" role="img" aria-label="Blue and red geometric cover design" style="background:linear-gradient(160deg,#2a3ea0,#b0304a)"></div></div>
  <div class="card" style="top:1678px;left:453px"><div class="phone dark" role="img" aria-label="Motivational lettering cover design" style="background:linear-gradient(160deg,#f4f0ea,#e7c7b8)"></div></div>
  <div class="card" style="top:1678px;left:769px"><div class="phone dark" role="img" aria-label="Black and white doodle cover design" style="background:linear-gradient(160deg,#f2f2f2,#9a9a9a)"></div></div>
  <div class="card-title" style="top:2031px;left:137px">Vexa Covers</div><div class="card-sub" style="top:2061px;left:137px">Vexa Nova S7</div>
  <div class="card-title" style="top:2031px;left:453px">Vexa Covers</div><div class="card-sub" style="top:2061px;left:453px">Vexa Nova S8</div>
  <div class="card-title" style="top:2031px;left:769px">Vexa Covers</div><div class="card-sub" style="top:2061px;left:769px">Vexa Nova S9</div>
  <div class="btn" style="top:2147px;left:481px;width:216px;height:50px">Show More</div>
</section>

<section>
  <div class="divider" style="top:2374px;left:150px;width:363px"></div>
  <div class="divider" style="top:2374px;left:681px;width:369px"></div>
  <div class="badge" style="top:2322px;left:543px">
    <svg width="56" height="56" viewBox="0 0 56 56" fill="none" stroke="#fff" stroke-width="5" stroke-linecap="round"><path d="M10 10 L46 46"/><path d="M46 10 L22 34"/><circle cx="14" cy="42" r="6"/><path d="M40 6 L50 16"/></svg></div>
  <h2 class="abs heading" style="top:2456px;font-size:62px">Choose your design</h2>
  <p class="abs subheading" style="top:2530px">Pick from one of our custom premade designs<br>below or upload your own</p>

  <div class="pattern" role="img" aria-label="Hand lettered motivational quote design" style="top:2656px;left:147px;background:linear-gradient(160deg,#f6f2ec,#e9b7a4)"></div>
  <div class="pattern" role="img" aria-label="Black and white doodle design" style="top:2656px;left:387px;background:linear-gradient(160deg,#f4f4f4,#8c8c8c)"></div>
  <div class="pattern" role="img" aria-label="Blue and red geometric design" style="top:2656px;left:631px;background:linear-gradient(160deg,#2c3c9e,#a8304e)"></div>
  <div class="pattern" role="img" aria-label="Purple starfield design" style="top:2656px;left:872px;background:linear-gradient(160deg,#8c2aa0,#402a8c)"></div>
  <div class="btn" style="top:2884px;left:484px;width:216px;height:50px">Show More</div>

  <div class="or">or</div>
  <div class="upload-field"><span class="cloud"></span>Choose your own design</div>
  <div class="btn" style="top:3088px;left:666px;width:215px;height:53px">Upload Files</div>
  <p class="hint">Accepted file types: JPG, PNG or PDF. Maximum file size is 10MB please.</p>
</section>

<section>
  <div class="divider" style="top:3290px;left:150px;width:363px"></div>
  <div class="divider" style="top:3290px;left:681px;width:369px"></div>
  <div class="badge" style="top:3238px;left:543px">
    <svg width="56" height="56" viewBox="0 0 56 56" fill="none" stroke="#fff" stroke-width="5" stroke-linecap="round"><path d="M10 10 L46 46"/><path d="M46 10 L22 34"/><circle cx="14" cy="42" r="6"/><path d="M40 6 L50 16"/></svg></div>
  <h2 class="abs heading" style="top:3372px;font-size:62px">Choose your phone</h2>
  <p class="abs subheading" style="top:3444px">Pick from Lumo or Vexa phone covers</p>

  <div class="card" style="top:3553px;left:225px;width:306px;height:403px"><div class="phone" role="img" aria-label="Cover preview with repeated heart pattern" style="width:150px;height:340px;background:linear-gradient(160deg,#fff,#f1dcdc)"></div></div>
  <div class="card" style="top:3553px;left:653px;width:306px;height:403px"><div class="phone dark" role="img" aria-label="Cover preview with repeated heart pattern" style="width:150px;height:340px;background:linear-gradient(160deg,#fff,#f1dcdc)"></div></div>
  <div class="card-title" style="top:3970px;left:225px;width:306px">Lumo Covers</div>
  <div class="card-title" style="top:3970px;left:653px;width:306px">Vexa Covers</div>
  <div class="select" style="top:4008px;left:300px">Lumo 7</div>
  <div class="select" style="top:4008px;left:728px">Vexa Nova S7</div>

  <div class="submit-box"></div>
  <div class="btn" style="top:4166px;left:306px;width:563px;height:47px;font-size:20px">Submit design now to receive your FREE phone cover</div>
  <p class="abs subheading postage">Enter your postage details on the next page</p>
</section>

<footer>
  <div class="abs footer"></div>
  <div class="abs brand footer-logo"><span class="brand-mark"></span><span class="brand-name">Kindred Prints</span></div>
  <div class="abs footer-phone">
    <svg width="22" height="22" viewBox="0 0 24 24"><path d="M6 2 L10 7 L8 10 Q10 14 14 16 L17 14 L22 18 L19 22 Q8 21 2 5 Z" fill="#e3140c"/></svg>07 700 900 412</div>
  <div class="footer-col" style="left:419px"><h4>WHAT WE DO</h4>Information here<br>Information here<br>Information here<br>Information here<br>Information here</div>
  <div class="footer-col" style="left:603px"><h4>INFORMATION</h4>Information here<br>Privacy Policy<br>Press Kit<br>FAQ</div>
  <div class="footer-col" style="left:791px"><h4>ABOUT</h4>Contacts<br>Team<br>Support</div>
  <div class="footer-col" style="left:928px"><h4>FOLLOW</h4>Chirpline<br>Friendboard<br>Searchly</div>
  <div class="abs legal">© Kindred Prints 2018. All Rights Reserved.</div>
</footer>

</body>
</html>
```